KT Appraisals BV business cards (a financial services company)

I am looking for a business card design that stands out in the financial advisory field of business & intellectual property valuation. The business card design should be conservative, yet different. Address details have changed since the attached business card. New address is:

Dorpelstraat 27
4817 KM Leiden
The Netherlands

Telephone number remains the same.

```html
<!DOCTYPE html>
<html lang="en">
<head>
<meta charset="utf-8">
<title>KT Appraisals BV – Business Card</title>
<link rel="stylesheet" href="https://fonts.googleapis.com/css2?family=Source+Sans+3:wght@300;400;600&display=swap">
<style>
  :root {
    --canvas-bg: #d9dadc;
    --card-dark: #1b1b1b;
    --card-light: #ffffff;
    --ink: #3a3a3a;
    --ink-soft: #555555;
    --rule: #8a8a8a;
  }
  * { box-sizing: border-box; margin: 0; padding: 0; }
  html, body {
    width: 1200px; height: 800px; overflow: hidden;
    background: var(--canvas-bg);
    font-family: "Source Sans 3", sans-serif;
    color: var(--ink);
  }
  .sheet {
    position: relative; width: 1200px; height: 800px;
    display: flex; flex-direction: column; align-items: center; justify-content: center; gap: 40px;
  }
  .card {
    position: relative; width: 595px; height: 340px;
    box-shadow: 0 2px 6px rgba(0,0,0,0.18);
  }
  .card-back { background: var(--card-dark); }
  .card-front { background: var(--card-light); }

  .contact { position: absolute; left: 40px; top: 62px; }
  .person-name { font-size: 20px; font-weight: 600; letter-spacing: 0.2px; }
  .credentials { font-size: 14px; font-weight: 600; }
  .person-role { font-size: 15px; font-weight: 400; color: var(--ink-soft); margin-top: 1px; }

  .divider {
    position: absolute; left: 40px; right: 40px; top: 128px;
    border-top: 1px solid var(--rule);
  }

  .address { position: absolute; left: 40px; top: 144px; font-size: 15px; line-height: 1.3; }
  .channels { position: absolute; left: 40px; top: 222px; list-style: none; font-size: 15px; line-height: 1.35; }
  .channels li { display: flex; align-items: center; gap: 7px; }
  .channels svg { width: 13px; height: 13px; fill: none; stroke: var(--ink); stroke-width: 1.6; }

  .brand-name {
    position: absolute; right: 40px; top: 70px;
    font-size: 26px; font-weight: 300; letter-spacing: 1.5px; text-transform: uppercase;
    color: var(--ink);
  }

  .tagline {
    position: absolute; right: 40px; bottom: 40px; text-align: right;
    font-size: 15px; line-height: 1.3; color: var(--ink);
  }
</style>
</head>
<body>
  <main class="sheet">
    <section class="card card-back" aria-label="Card back"></section>

    <section class="card card-front" aria-label="Card front">
      <div class="contact">
        <p class="person-name">Maarten Vos, <span class="credentials">CFA, ASA, RV</span></p>
        <p class="person-role">Managing Director</p>
      </div>

      <p class="brand-name">KT Appraisals</p>

      <div class="divider"></div>

      <address class="address" style="font-style: normal;">
        Dorpelstraat 27<br>
        4817 KM Leiden<br>
        The Netherlands
      </address>

      <ul class="channels">
        <li>
          <svg viewBox="0 0 16 16" aria-hidden="true"><path d="M4 2l2.5 3-1.5 1.5c.8 1.8 2.2 3.2 4 4L10.5 9 13.5 11.5 12 14C7 13.5 2.5 9 2 4z" fill="#3a3a3a" stroke="none"/></svg>
          +31 (0)70 555 0142
        </li>
        <li>
          <svg viewBox="0 0 16 16" aria-hidden="true"><rect x="1.5" y="3.5" width="13" height="9"/><path d="M1.5 3.5L8 9l6.5-5.5"/></svg>
          mvos@ktappraisals.com
        </li>
        <li>
          <svg viewBox="0 0 16 16" aria-hidden="true"><circle cx="8" cy="8" r="6.3"/><path d="M1.7 8h12.6M8 1.7c-3 3.4-3 9.2 0 12.6M8 1.7c3 3.4 3 9.2 0 12.6"/></svg>
          www.ktappraisals.com
        </li>
      </ul>

      <p class="tagline">Business and Intellectual<br>Property Valuations</p>
    </section>
  </main>
</body>
</html>
```